All Out No Regrets Art

I'd like my motto "All Out No Regrets" made into art for my office. I'm in a very formal/conservative office building but my office is more modern and upbeat. Even though the motto sounds really bold and maybe even harsh, I'm looking for something upbeat and happy. Nothing too harsh/angular, I like swirls and modern whimsical things. Love the colors orange, gray and bright/lime green but it doesn't have to be just those colors or all those colors. I do NOT like navy blue and burgandy.
This needs to look like high-quality art, not like a "poster" because it's for an executive office.
I've updated the creative brief.
Building

```html
<!DOCTYPE html>
<html lang="en">
<head>
<meta charset="utf-8">
<title>All Out No Regrets</title>
<link rel="stylesheet" href="https://fonts.googleapis.com/css2?family=Righteous&display=swap">
<style>
  :root {
    --cream: #fff6e0;
    --pale-yellow: #ffe79a;
    --sunflower: #fdc23a;
    --amber: #f7a12a;
    --tangerine: #f26a21;
    --coral: #f5815a;
    --rose-red: #f0284f;
    --label-white: #fffdfc;
    --lime: #d4de1f;
  }

  * { margin: 0; padding: 0; box-sizing: border-box; }

  html, body {
    width: 1200px;
    height: 756px;
    overflow: hidden;
    background: var(--cream);
  }

  .artwork {
    position: relative;
    width: 1200px;
    height: 756px;
    overflow: hidden;
  }

  .swirl-backdrop {
    position: absolute;
    inset: 0;
    background:
      radial-gradient(ellipse 360px 260px at 60px 740px, var(--rose-red) 0%, rgba(240,40,79,0.55) 45%, rgba(240,40,79,0) 100%),
      radial-gradient(ellipse 300px 200px at 520px 760px, rgba(240,60,70,0.85) 0%, rgba(240,60,70,0) 100%),
      radial-gradient(ellipse 420px 300px at 560px 430px, rgba(255,250,235,0.95) 0%, rgba(255,250,235,0) 100%),
      radial-gradient(ellipse 380px 220px at 1120px 200px, rgba(255,240,190,0.9) 0%, rgba(255,240,190,0) 100%),
      radial-gradient(ellipse 340px 320px at 700px 140px, rgba(242,106,33,0.9) 0%, rgba(242,106,33,0) 100%),
      radial-gradient(ellipse 380px 300px at 980px 420px, rgba(247,140,40,0.85) 0%, rgba(247,140,40,0) 100%),
      radial-gradient(ellipse 360px 220px at 120px 320px, rgba(255,243,215,0.95) 0%, rgba(255,243,215,0) 100%),
      radial-gradient(ellipse 300px 240px at 200px 60px, rgba(253,194,58,0.9) 0%, rgba(253,194,58,0) 100%),
      linear-gradient(160deg, var(--amber) 0%, var(--sunflower) 30%, var(--pale-yellow) 55%, var(--coral) 100%);
  }

  .motto-label {
    position: absolute;
    display: flex;
    align-items: center;
    background: var(--label-white);
    border-radius: 16px;
    font-family: "Righteous", sans-serif;
    color: var(--lime);
    line-height: 1;
    white-space: nowrap;
  }

  .motto-label--first {
    left: -16px;
    top: 525px;
    width: 478px;
    height: 135px;
    padding-left: 64px;
    font-size: 104px;
  }

  .motto-label--second {
    left: 515px;
    top: 605px;
    width: 701px;
    height: 133px;
    padding-left: 64px;
    font-size: 104px;
  }
</style>
</head>
<body>
  <main class="artwork">
    <div class="swirl-backdrop" role="img" aria-label="Low-poly swirl pattern of triangles in orange, yellow, cream and red"></div>
    <h1 class="motto-label motto-label--first">All Out</h1>
    <p class="motto-label motto-label--second">No Regrets</p>
  </main>
</body>
</html>
```